Nana Bo's needs your help creating a clean, simple, possibly vintage style label for a natural rem...

We need a label for a new product to be sold in local stores. It will be a bottle of fresh Elderberry Syrup which is a natural remedy for the flu, colds, and allergies. Our syrup is different from others in the market as it is fresh, needs to be refrigerated, and does not include preservatives, added sugar, alcohol, or anything artificial. We would like a label with easy to read text, with a clean or vintage look. We would like a 3 inch by 3 inch circle front label with mostly text, not too busy, and possibly a branch of elderberries may be included. We also need a 3 inch by 3 inch circle label for the back of the bottle with the nutrition facts, ingredients, dosage, and specific text. Both labels should be lighter in (background) color to stand out from the dark purple liquid inside. We're leaning towards black for the main text, but open to other ideas that are neutral and not too flashy.The final design should be clear, clean, making the main text visible if in a grocery store refrigerator. It should appeal to all, but mostly to natural minded mothers.
Natural minded mothers

```html
<!DOCTYPE html>
<html lang="en">
<head>
<meta charset="utf-8">
<title>Nana Bo's Elderberry Syrup – Front Label</title>
<link rel="stylesheet" href="https://fonts.googleapis.com/css2?family=Passion+One:wght@400;700&family=Roboto+Slab:wght@400;700&display=swap">
<style>
  :root {
    --backdrop: #ecebe8;
    --label-white: #ffffff;
    --ink: #1d1d1d;
    --ink-soft: #5a5a5a;
    --berry: #7a3fa3;
    --berry-light: #b48fd0;
    --leaf-green: #8cc63f;
    --edge: #d8d6d2;
  }
  html, body {
    margin: 0;
    padding: 0;
    width: 1200px;
    height: 1200px;
    overflow: hidden;
    background: var(--backdrop);
  }
  .label {
    display: block;
    width: 1200px;
    height: 1200px;
  }
  .label-disc { fill: var(--label-white); stroke: var(--edge); stroke-width: 2; }
  .label-ring { fill: none; stroke: var(--ink); stroke-width: 13; }
  .label-ring-inner { fill: none; stroke: var(--ink); stroke-width: 3; }
  .arc-text {
    font-family: "Roboto Slab", Georgia, serif;
    font-weight: 700;
    font-size: 36px;
    letter-spacing: 1px;
    fill: var(--ink);
  }
  .brand-name {
    font-family: "Roboto Slab", Georgia, serif;
    font-weight: 700;
    font-size: 58px;
    fill: var(--ink);
  }
  .product-title {
    font-family: "Passion One", Impact, sans-serif;
    font-weight: 700;
    fill: var(--berry);
    stroke: var(--berry-light);
    stroke-width: 2;
    paint-order: stroke;
  }
  .product-title--main { font-size: 150px; }
  .product-title--sub { font-size: 138px; }
  .net-weight {
    font-family: "Roboto Slab", Georgia, serif;
    font-weight: 700;
    font-size: 21px;
    fill: var(--ink);
  }
  .benefit {
    font-family: "Roboto Slab", Georgia, serif;
    font-weight: 700;
    font-size: 30px;
    letter-spacing: 1px;
    fill: var(--leaf-green);
  }
  .remedy-note {
    font-family: "Roboto Slab", Georgia, serif;
    font-weight: 400;
    font-size: 16px;
    letter-spacing: 0.5px;
    fill: var(--ink-soft);
  }
</style>
</head>
<body>
<svg class="label" viewBox="0 0 1200 1200" xmlns="http://www.w3.org/2000/svg" aria-label="Nana Bo's Elderberry Syrup front label">
  <defs>
    <path id="arc-top" d="M 205,600 A 395 395 0 0 1 995,600"/>
    <path id="arc-bottom" d="M 172,600 A 428 428 0 0 0 1028,600"/>
    <linearGradient id="berry-sprig-fill" x1="0" y1="0" x2="1" y2="1">
      <stop offset="0" stop-color="#7fb24a"/>
      <stop offset="0.45" stop-color="#8d6bb3"/>
      <stop offset="1" stop-color="#5a2d80"/>
    </linearGradient>
  </defs>

  <circle class="label-disc" cx="600" cy="600" r="500"/>
  <circle class="label-ring" cx="600" cy="600" r="458"/>
  <circle class="label-ring-inner" cx="600" cy="600" r="350"/>

  <text class="arc-text">
    <textPath href="#arc-top" startOffset="50%" text-anchor="middle">MADE WITH ORGANIC ELDERBERRIES &amp; SPICES</textPath>
  </text>
  <text class="arc-text">
    <textPath href="#arc-bottom" startOffset="50%" text-anchor="middle">AND LOCAL TEXAS RAW HONEY</textPath>
  </text>

  <text class="brand-name" x="600" y="400" text-anchor="middle">Nana Bo's</text>

  <text class="product-title product-title--main" x="600" y="545" text-anchor="middle" textLength="640" lengthAdjust="spacingAndGlyphs">ELDERBERRY</text>

  <rect class="berry-sprig" x="318" y="560" width="150" height="160" rx="70" fill="url(#berry-sprig-fill)" role="img" aria-label="Illustration of an elderberry sprig with green leaves and a purple berry cluster"/>

  <text class="product-title product-title--sub" x="640" y="678" text-anchor="middle" textLength="320" lengthAdjust="spacingAndGlyphs">SYRUP</text>

  <text class="net-weight" x="862" y="608" text-anchor="middle">NET WT</text>
  <text class="net-weight" x="862" y="633" text-anchor="middle">8 FL OZ</text>

  <text class="benefit" x="640" y="722" text-anchor="middle">IMMUNE BOOSTING</text>

  <text class="remedy-note" x="640" y="752" text-anchor="middle">NATURAL REMEDY FOR THE FLU,</text>
  <text class="remedy-note" x="640" y="772" text-anchor="middle">COLDS, AND ALLERGIES</text>
</svg>
</body>
</html>
```